Design for schnapps bottle label "Sol Terrado"

Hi! On a small land lot we are producing our own Italian schnapps "Grappa". For the bottles we would like to modernize our current labes that you find below. The two cats looking at each other should remain, but updated and more modern. I am very much looking forward to your suggestions. Best, Joel

Target Market(s)

Schnapps bottle label

Requirements
Must have
• Cats should resemble the cats that are decorating the house entry (see attached), however, should have a more modern appearance.

Text elements should remain: "Grappa", "Sol Terrado", "Legnoso", "[Vintage Year], "Raccolta No", "Vol %"
Should not have
• Current ornament can be used, replaced or deleted (whatever looks best)

```html
<!DOCTYPE html>
<html lang="it">
<head>
<meta charset="utf-8">
<title>Grappa Legnoso 2015 – Sol Terrado</title>
<link rel="stylesheet" href="https://fonts.googleapis.com/css2?family=Big+Shoulders+Inline+Display:wght@800&family=Kaushan+Script&display=swap">
<style>
  :root {
    --label-red: #ee4b3e;
    --label-orange: #f7941d;
    --label-yellow: #fde23a;
    --ink: #0c0c0c;
    --ink-shadow: rgba(60, 40, 20, 0.55);
    --art-dark: #1a1410;
    --art-warm: #3a2a18;
    --page: #ffffff;
  }
  html, body {
    margin: 0;
    padding: 0;
    width: 1200px;
    height: 1200px;
    overflow: hidden;
    background: var(--page);
  }
  .label-canvas {
    display: block;
    width: 1200px;
    height: 1200px;
  }
  .title-word {
    font-family: "Big Shoulders Inline Display", "Bebas Neue", sans-serif;
    font-weight: 800;
    font-size: 360px;
  }
  .cuvee-line {
    font-family: "Kaushan Script", cursive;
    font-size: 84px;
  }
  .footer-note {
    font-family: "Kaushan Script", cursive;
    font-size: 32px;
  }
  .ink { fill: var(--ink); }
  .ink-shadow { fill: var(--ink-shadow); }
  .rule { fill: var(--ink); }
  .frame-line { stroke: var(--ink); stroke-width: 2; fill: none; }
  .art-area { opacity: 0.85; }
</style>
</head>
<body>
<svg class="label-canvas" viewBox="0 0 1200 1200" xmlns="http://www.w3.org/2000/svg">
  <defs>
    <linearGradient id="labelGradient" x1="0" y1="0" x2="0.55" y2="1">
      <stop offset="0" stop-color="var(--label-red)"/>
      <stop offset="0.5" stop-color="var(--label-orange)"/>
      <stop offset="1" stop-color="var(--label-yellow)"/>
    </linearGradient>
    <linearGradient id="artGradient" x1="0" y1="0" x2="1" y2="1">
      <stop offset="0" stop-color="var(--art-dark)"/>
      <stop offset="1" stop-color="var(--art-warm)"/>
    </linearGradient>
  </defs>

  <!-- label ground -->
  <rect class="label-ground" x="217" y="48" width="780" height="1101" fill="url(#labelGradient)"/>

  <!-- frame -->
  <g class="frame">
    <line class="frame-line" x1="326" y1="73" x2="891" y2="73"/>
    <line class="frame-line" x1="326" y1="79" x2="891" y2="79"/>
    <line class="frame-line" x1="234" y1="150" x2="234" y2="1045"/>
    <line class="frame-line" x1="240" y1="150" x2="240" y2="1045"/>
    <line class="frame-line" x1="974" y1="150" x2="974" y2="1045"/>
    <line class="frame-line" x1="980" y1="150" x2="980" y2="1045"/>
  </g>

  <!-- ornament areas -->
  <rect class="art-area ornament-top" x="482" y="98" width="278" height="38" rx="19" fill="url(#artGradient)" role="img" aria-label="Scrolled flourish ornament"/>
  <rect class="art-area ornament-corner" x="223" y="56" width="62" height="84" rx="14" fill="url(#artGradient)" role="img" aria-label="Corner flourish"/>
  <rect class="art-area ornament-corner" x="929" y="56" width="62" height="84" rx="14" fill="url(#artGradient)" role="img" aria-label="Corner flourish"/>
  <rect class="art-area ornament-corner" x="223" y="1050" width="62" height="62" rx="14" fill="url(#artGradient)" role="img" aria-label="Corner flourish"/>
  <rect class="art-area ornament-corner" x="929" y="1050" width="62" height="62" rx="14" fill="url(#artGradient)" role="img" aria-label="Corner flourish"/>

  <!-- title rules -->
  <g class="title-rules">
    <rect class="rule" x="394" y="192" width="543" height="7"/>
    <rect class="rule" x="394" y="206" width="543" height="4"/>
    <rect class="rule" x="286" y="492" width="308" height="4"/>
    <rect class="rule" x="286" y="502" width="308" height="7"/>
    <rect class="rule" x="789" y="492" width="157" height="4"/>
    <rect class="rule" x="789" y="502" width="157" height="7"/>
  </g>

  <!-- product name -->
  <g class="title">
    <text class="title-word ink-shadow" x="291" y="484" textLength="660" lengthAdjust="spacingAndGlyphs">Grappa</text>
    <text class="title-word ink" x="284" y="478" textLength="660" lengthAdjust="spacingAndGlyphs">Grappa</text>
  </g>

  <!-- cuvée and vintage -->
  <g class="cuvee">
    <text class="cuvee-line ink-shadow" x="297" y="666" textLength="586" lengthAdjust="spacingAndGlyphs">“Legnoso” 2015</text>
    <text class="cuvee-line ink" x="291" y="660" textLength="586" lengthAdjust="spacingAndGlyphs">“Legnoso” 2015</text>
  </g>

  <!-- cats illustration area -->
  <rect class="art-area cats-illustration" x="300" y="714" width="654" height="309" rx="40" fill="url(#artGradient)" role="img" aria-label="Two black cat silhouettes playfully facing each other"/>

  <!-- footer details -->
  <g class="footer">
    <text class="footer-note ink-shadow" x="314" y="1078" textLength="254" lengthAdjust="spacingAndGlyphs">Raccolta N°. 01</text>
    <text class="footer-note ink" x="311" y="1075" textLength="254" lengthAdjust="spacingAndGlyphs">Raccolta N°. 01</text>
    <text class="footer-note ink-shadow" x="753" y="1078" textLength="168" lengthAdjust="spacingAndGlyphs">41.0% Vol.</text>
    <text class="footer-note ink" x="750" y="1075" textLength="168" lengthAdjust="spacingAndGlyphs">41.0% Vol.</text>
  </g>
</svg>
</body>
</html>
```